Graphic Design/Logo Needed for Ear Drops Bottle

We have an Ear Drop Medication that we need to create a new label for. We will use a retro picture of a Doctor (Dr. Blenham) and the name of the product is Tidy Lobe. There is no official logo, so we will want to create a retro, basic logo for Tidy Lobe and use the retro picture. Front portion of the label is Size is 1.5" in height, and about 1.375" Width. this is a small tube similar in size to eye drops. We will be looking for just the logo portion and what you will see on the front of the bottle.

Target Market(s)

Medical Container

Industry/Entity Type

Medical

Font styles to use
Serif
Sans Serif

Colors
0054AA
0677BA
7BADD7
CADEEF
E8F1F8
FFF300
FFF600
FEFA6F
FFFEC7
FFFEE8

Requirements
Must have
• Picture of Dr. Blenham, "Tidy Lobe", Dr. Blenham's Ear Solution
Nice to have
• Retro Style or Modern with Retro Feel, Clean and engaging

```html
<!DOCTYPE html>
<html lang="en">
<head>
<meta charset="utf-8">
<title>Tidy Lobe – Dr. Blenham's Ear Solution Label</title>
<link href="https://fonts.googleapis.com/css2?family=Squada+One&family=Cinzel:wght@500;700&display=swap" rel="stylesheet">
<style>
  :root {
    --backdrop: #e4e4e4;
    --paper: #f3e9da;
    --paper-deep: #eadcc6;
    --teal: #3a9aa6;
    --teal-dark: #1f7681;
    --red: #e2463a;
    --cream-text: #f6efe2;
    --portrait-light: #e9dfcf;
    --portrait-dark: #8a8174;
  }
  * { margin: 0; padding: 0; box-sizing: border-box; }
  html, body {
    width: 1200px; height: 1200px; overflow: hidden;
    background: var(--backdrop);
  }
  .label {
    position: absolute;
    left: 250px; top: 100px;
    width: 700px; height: 1000px;
    background: radial-gradient(ellipse at 50% 40%, var(--paper) 55%, var(--paper-deep) 100%);
    overflow: hidden;
  }
  .torn-band {
    position: absolute; left: 0; width: 700px; height: 70px;
  }
  .torn-band--top { top: 0; }
  .torn-band--bottom { bottom: 0; }
  .portrait {
    position: absolute;
    left: 165px; top: 130px;
    width: 370px; height: 240px;
    background: radial-gradient(ellipse at 50% 45%, var(--portrait-dark) 0%, #b3a898 45%, var(--portrait-light) 80%, transparent 100%);
  }
  .product-name {
    position: absolute; left: 0; top: 385px; width: 700px;
    text-align: center;
    font-family: "Squada One", sans-serif;
    font-size: 118px; line-height: 1;
    letter-spacing: 3px;
    color: var(--teal);
    text-transform: uppercase;
  }
  .maker-name {
    position: absolute; left: 0; top: 590px; width: 700px;
    text-align: center;
    font-family: "Cinzel", serif;
    font-weight: 500;
    font-size: 60px; line-height: 1;
    color: var(--red);
  }
  .ribbon {
    position: absolute; left: 40px; top: 690px;
    width: 620px; height: 110px;
  }
  .ribbon-text {
    position: absolute; left: 0; top: 712px; width: 700px;
    text-align: center;
    font-family: "Cinzel", serif;
    font-weight: 700;
    font-size: 58px; line-height: 66px;
    color: var(--cream-text);
  }
  .rule {
    position: absolute; left: 40px; top: 840px;
    width: 620px; height: 5px;
    background: var(--red);
  }
  .flourish {
    position: absolute; left: 230px; top: 858px;
    width: 240px; height: 50px;
    background: radial-gradient(ellipse at 50% 40%, rgba(226,70,58,0.75) 0%, rgba(226,70,58,0.25) 60%, transparent 100%);
  }
</style>
</head>
<body>
  <main class="label">
    <svg class="torn-band torn-band--top" viewBox="0 0 700 70" preserveAspectRatio="none" aria-hidden="true">
      <path fill="var(--teal)" d="M0 0 H700 V34 L688 40 L670 32 L648 44 L630 36 L604 46 L580 38 L556 48 L530 40 L505 45 L480 37 L452 47 L430 39 L400 46 L372 38 L350 44 L320 36 L296 46 L270 40 L240 48 L215 38 L190 46 L160 38 L135 47 L110 40 L85 48 L60 38 L38 46 L18 36 L0 42 Z"/>
    </svg>

    <div class="portrait" role="img" aria-label="Retro sepia portrait of Dr. Blenham wearing a head mirror and white coat"></div>

    <h1 class="product-name">Tidy Lobe</h1>
    <p class="maker-name">DR. BLENHAM'S</p>

    <svg class="ribbon" viewBox="0 0 620 110" aria-hidden="true">
      <path fill="var(--teal-dark)" d="M0 30 H60 V95 H0 L22 62 Z"/>
      <path fill="var(--teal-dark)" d="M620 30 H560 V95 H620 L598 62 Z"/>
      <rect x="35" y="14" width="550" height="76" fill="var(--teal)"/>
    </svg>
    <p class="ribbon-text">EAR SOLUTION</p>

    <div class="rule"></div>
    <div class="flourish" role="img" aria-label="Small red decorative flourish"></div>

    <svg class="torn-band torn-band--bottom" viewBox="0 0 700 70" preserveAspectRatio="none" aria-hidden="true">
      <path fill="var(--teal)" d="M0 70 H700 V30 L680 24 L660 34 L636 26 L612 36 L588 28 L560 34 L536 24 L510 32 L484 26 L458 36 L430 28 L404 34 L380 24 L352 32 L326 26 L300 36 L272 28 L246 34 L220 24 L194 32 L168 26 L140 36 L114 28 L88 34 L62 24 L36 32 L16 26 L0 32 Z"/>
    </svg>
  </main>
</body>
</html>
```